New AI Company Needs a Powerpoint

We are a new type of AI company called KindredAI. Our AI uses human inspired approaches and put the human on the center of all our solutions. We need a standard company powerpoint design to use with potential investors, customers and partners to introduce our company and explain how the approach we take to AI is very different than others.
We want a design that is clean, modern, and playful. We do not want it to look overly robotic or cliche techy. Our mission is to remind the world that technology is a tool to be used to enhance and assist not to replace real humans.
We want a design that can show boring things (like financial info) in engaging ways.

Please use colors in logo variations along with a vibrant complementary color palette of your choosing,

Industry/Entity Type

Technology

Font styles to use
Sans Serif
Other font styles liked:
• Opensans

Colors
0054AA
0677BA
7BADD7
CADEEF
E8F1F8
0094D4
00A9DD
6FCCEA
C7EBF8
E9F6FB
00AB8E
00BBA5
67D7C9
C6EFE9
E9F9F6
59FF00
82FF00
B8FF75
E3FFCB
F4FFEA

Requirements
Must have
• Must incorporate logo colors and style

```html
<!DOCTYPE html>
<html lang="en">
<head>
<meta charset="utf-8">
<title>KindredAI – Company Deck</title>
<link rel="stylesheet" href="https://fonts.googleapis.com/css2?family=Montserrat:wght@500;600;700&family=Open+Sans:wght@400;600&display=swap">
<style>
:root{
  --stage:#8c8c8c;
  --navy:#181a33;
  --navy-deep:#1f2a4d;
  --blue:#0677ba;
  --blue-bright:#1a8ad0;
  --sky:#7badd7;
  --pale:#cadeef;
  --mist:#e8f1f8;
  --ink:#2a2a2a;
  --muted:#555b66;
  --white:#ffffff;
}
*{box-sizing:border-box;margin:0;padding:0}
html,body{width:1200px;height:4231px;overflow:hidden}
body{background:var(--stage);position:relative;font-family:"Open Sans",Arial,sans-serif;color:var(--ink)}
.slide{position:absolute;left:60px;width:1080px;height:607px;overflow:hidden;background:var(--white)}
.heading{font-family:"Montserrat",Arial,sans-serif;font-weight:600;font-size:20px;color:#222;letter-spacing:.2px}
.heading::after{content:"";display:block;width:32px;height:3px;background:var(--blue);margin-top:8px}
.side-band{position:absolute;left:0;top:0;width:56px;height:100%;background:linear-gradient(180deg,var(--blue) 0%,var(--navy-deep) 100%)}
.badge{position:absolute;left:18px;top:49px;width:100px;height:100px;border-radius:50%;background:var(--white);box-shadow:0 4px 14px rgba(0,0,0,.15);display:flex;align-items:center;justify-content:center;font-family:"Montserrat",Arial,sans-serif;font-weight:700;font-size:13px;color:var(--blue)}
.body-text{font-size:11.5px;line-height:18px;color:var(--muted)}
.photo{position:absolute}

/* Slide 1 */
.cover{top:84px;background:var(--navy)}
.cover-art{left:560px;top:90px;width:500px;height:440px;background:radial-gradient(ellipse at 60% 50%,rgba(26,138,208,.85) 0%,rgba(6,119,186,.45) 45%,rgba(24,26,51,0) 72%)}
.cover-name{position:absolute;left:50px;top:272px;font-family:"Montserrat",Arial,sans-serif;font-weight:600;font-size:116px;letter-spacing:4px;color:var(--white);line-height:1}
.social{position:absolute;left:50px;top:523px;display:flex;gap:6px}
.social span{width:33px;height:33px;border:1.5px solid var(--white);border-radius:50%}

/* Slide 2 */
.about{top:760px}
.about .heading{position:absolute;left:159px;top:88px}
.about .intro{position:absolute;left:159px;top:150px;width:395px;text-align:justify}
.checks{position:absolute;left:159px;top:250px;width:430px;list-style:none}
.checks li{position:relative;padding-left:30px;margin-bottom:22px}
.checks svg{position:absolute;left:0;top:3px}
.about-photo{left:658px;top:0;width:422px;height:607px;background:linear-gradient(160deg,#1c3350 0%,#0d1a2e 55%,#07101d 100%)}

/* Slide 3 */
.services{top:1448px}
.services .heading{position:absolute;left:159px;top:88px}
.hub{position:absolute;left:136px;top:156px;width:388px;height:388px;border-radius:50%;background:var(--mist);display:flex;align-items:center;justify-content:center}
.hub-inner{width:330px;height:330px;border-radius:50%;background:var(--white);border:10px solid var(--pale);display:flex;align-items:center;justify-content:center;font-family:"Montserrat",Arial,sans-serif;font-weight:600;font-size:36px;color:var(--navy-deep)}
.service{position:absolute;width:320px}
.service h3{font-family:"Montserrat",Arial,sans-serif;font-weight:500;font-size:17px;color:#222;margin-bottom:10px}
.service p{font-size:10.5px;line-height:19px;color:var(--muted)}
.flow{position:absolute;left:0;top:0}

/* Slide 4 */
.investors{top:2139px;background:linear-gradient(90deg,#f7f9fc 0%,#eef2f8 45%,#e3eaf3 100%)}
.investors-bg{left:520px;top:0;width:560px;height:607px;background:radial-gradient(ellipse at 35% 35%,rgba(160,175,200,.35) 0%,rgba(230,236,245,0) 65%)}
.investors .heading{position:absolute;left:159px;top:86px}
.investors-photo{left:146px;top:179px;width:322px;height:322px;border-radius:50%;background:radial-gradient(circle at 40% 45%,#c9772e 0%,#3a2a3a 30%,#0e1830 70%);border-right:5px solid var(--blue-bright)}
.investors .copy{position:absolute;left:596px;top:158px;width:316px;font-size:11px;line-height:22.5px;color:var(--muted)}

/* Slide 5 */
.partners{top:2842px;background:linear-gradient(90deg,#f2f5fa 0%,#e6ecf5 100%)}
.partners .heading{position:absolute;left:159px;top:88px}
.partner-grid{position:absolute;left:118px;top:207px;display:grid;grid-template-columns:repeat(4,184px);grid-auto-rows:82px;column-gap:36px;row-gap:24px}
.partner{background:var(--white);border-radius:8px;box-shadow:0 3px 10px rgba(30,50,90,.12);display:flex;align-items:center;justify-content:center}
.partner i{display:block;width:36px;height:36px;background:var(--pale)}
.partner i.round{border-radius:50%}
.partner i.tone-a{background:var(--sky)}
.partner i.tone-b{background:var(--navy-deep)}

/* Slide 6 */
.closing{top:3538px}
.closing-photo{left:0;top:0;width:700px;height:607px}
.closing-name{position:absolute;left:740px;top:106px;width:240px;text-align:center;font-family:"Montserrat",Arial,sans-serif;font-weight:600;font-size:30px;color:var(--navy-deep)}
.thanks{position:absolute;left:658px;top:212px;width:330px;display:flex;align-items:center;gap:14px;font-family:"Montserrat",Arial,sans-serif;font-weight:700;font-size:38px;color:var(--blue-bright)}
.thanks::before,.thanks::after{content:"";flex:1;height:2px;background:var(--blue-bright)}
.presenter{position:absolute;left:732px;top:316px;font-family:"Montserrat",Arial,sans-serif;font-weight:600;font-size:17px;color:#222}
.contacts{position:absolute;left:732px;top:364px;list-style:none;font-size:11.5px;color:var(--muted)}
.contacts li{display:flex;align-items:flex-start;gap:14px;height:38px}
.contacts svg{flex:none;width:16px;height:16px;fill:#222}
</style>
</head>
<body>

<section class="slide cover">
  <div class="photo cover-art" role="img" aria-label="Glowing blue abstract head made of circuit lines"></div>
  <div class="cover-name">KINDREDAI</div>
  <div class="social"><span></span><span></span><span></span><span></span></div>
</section>

<section class="slide about">
  <div class="side-band"></div>
  <div class="badge">KindredAI</div>
  <h2 class="heading">OUR KINDRED</h2>
  <p class="body-text intro">Lorem ipsum dolor sit amet, consectetur adipiscing elit, sed do eiusmod tempor incididunt ut labore et dolore magna aliqua. Ut enim ad minim veniam, quis nostrud exercitation ullamco laboris nisi ut aliquip ex ea commodo consequat.</p>
  <ul class="checks body-text">
    <li><svg width="14" height="14" viewBox="0 0 14 14"><circle cx="7" cy="7" r="6" fill="none" stroke="#0677ba" stroke-width="1.2"/><path d="M4 7.2l2 2 4-4.4" fill="none" stroke="#0677ba" stroke-width="1.3"/></svg>Lorem ipsum dolor sit amet, consectetur adipiscing elit, sed do teiusmod tempor incididunt ut labore et dolore magna aliqua. Ut enim ad minim veniam, quis.</li>
    <li><svg width="14" height="14" viewBox="0 0 14 14"><circle cx="7" cy="7" r="6" fill="none" stroke="#0677ba" stroke-width="1.2"/><path d="M4 7.2l2 2 4-4.4" fill="none" stroke="#0677ba" stroke-width="1.3"/></svg>Lorem ipsum dolor sit amet, consectetur adipiscing elit, sed do eiusmod tempor incididunt ut labore et dolore magna aliqua.</li>
    <li><svg width="14" height="14" viewBox="0 0 14 14"><circle cx="7" cy="7" r="6" fill="none" stroke="#0677ba" stroke-width="1.2"/><path d="M4 7.2l2 2 4-4.4" fill="none" stroke="#0677ba" stroke-width="1.3"/></svg>Lorem ipsum dolor sit amet, consectetur adipiscing elit, sed do eiusmod tempor incididunt ut labore et dolore magna aliqua.</li>
  </ul>
  <div class="photo about-photo" role="img" aria-label="Woman working on a tablet in a dark control room with screens"></div>
</section>

<section class="slide services">
  <div class="side-band"></div>
  <div class="badge">KindredAI</div>
  <h2 class="heading">OUR SERVICES</h2>
  <div class="hub"><div class="hub-inner">KINDREDAI</div></div>
  <svg class="flow" width="1080" height="607" viewBox="0 0 1080 607">
    <path d="M474 115 C560 120 640 190 640 300 C640 420 580 540 474 558" fill="none" stroke="#333" stroke-width="1.2" stroke-dasharray="3 3"/>
    <circle cx="474" cy="115" r="4" fill="#999"/>
    <circle cx="474" cy="558" r="4" fill="#999"/>
    <polygon points="540,148 610,92 602,190" fill="#1a8ad0"/>
    <circle cx="573" cy="140" r="11" fill="none" stroke="#fff" stroke-width="1.5"/>
    <polygon points="598,215 680,205 640,295" fill="#1f2a4d"/>
    <circle cx="640" cy="232" r="11" fill="none" stroke="#fff" stroke-width="1.5"/>
    <polygon points="626,336 712,346 650,415" fill="#1a8ad0"/>
    <circle cx="664" cy="360" r="11" fill="none" stroke="#fff" stroke-width="1.5"/>
    <polygon points="548,525 628,460 630,535" fill="#1a8ad0"/>
    <circle cx="600" cy="508" r="11" fill="none" stroke="#fff" stroke-width="1.5"/>
  </svg>
  <div class="service" style="left:663px;top:94px"><h3>Artificial Intelligence</h3><p>Lorem ipsum dolor sit amet, consectetur adipiscing elit,<br>sed do eiusmod tempor incididunt ut labore</p></div>
  <div class="service" style="left:729px;top:212px"><h3>Computer</h3><p>Lorem ipsum dolor sit amet, consectetur adipiscing elit,<br>sed do eiusmod tempor incididunt ut labore</p></div>
  <div class="service" style="left:745px;top:350px"><h3>Human inspired</h3><p>Lorem ipsum dolor sit amet, consectetur adipiscing elit,<br>sed do eiusmod tempor incididunt ut labore</p></div>
  <div class="service" style="left:696px;top:473px"><h3>Technology</h3><p>Lorem ipsum dolor sit amet, consectetur adipiscing elit,<br>sed do eiusmod tempor incididunt ut labore</p></div>
</section>

<section class="slide investors">
  <div class="photo investors-bg" role="img" aria-label="Faded portrait of a man in glasses with technology overlay"></div>
  <div class="side-band"></div>
  <div class="badge">KindredAI</div>
  <h2 class="heading">POTENTIAL INVESTORS</h2>
  <div class="photo investors-photo" role="img" aria-label="Hand touching a glowing AI chip interface"></div>
  <p class="copy">Lorem ipsum dolor sit amet, consectetur adipiscing elit, sed do eiusmod tempor incididunt ut labore et dolore magna aliqua. Ut enim ad minim veniam, quis nostrud exercitation ullamco laboris nisi ut aliquip ex ea commodo consequat. Duis aute irure dolor in reprehenderit in voluptate velit esse cillum dolore eu fugiat nulla pariatur. Excepteur sint occaecat cupidatat non proident, sunt in culpa qui officia deserunt mollit anim id est laborum. Sed ut perspiciatis unde omnis iste natus error sit voluptatem accusantium doloremque laudantium, totam rem aperiam, eaque ipsa quae ab illo inventore veritatis et quasi architecto beatae vitae dicta sunt explicabo. Nemo enim ipsam voluptatem quia voluptas sit aspernatur aut odit aut fugit, sed quia consequuntur magni dolores eos qui ratione voluptatem sequi nesciunt.</p>
</section>

<section class="slide partners">
  <div class="side-band"></div>
  <div class="badge">KindredAI</div>
  <h2 class="heading">CUSTOMERS AND PARTNERS</h2>
  <div class="partner-grid">
    <div class="partner"><i class="round tone-a"></i></div>
    <div class="partner"><i class="tone-b"></i></div>
    <div class="partner"><i class="round"></i></div>
    <div class="partner"><i class="round tone-a"></i></div>
    <div class="partner"><i class="round"></i></div>
    <div class="partner"><i class="round tone-a"></i></div>
    <div class="partner"><i class="tone-b"></i></div>
    <div class="partner"><i class="round tone-a"></i></div>
    <div class="partner"><i class="tone-b"></i></div>
    <div class="partner"><i class="round"></i></div>
    <div class="partner"><i class="tone-b"></i></div>
    <div class="partner"><i class="round tone-a"></i></div>
  </div>
</section>

<section class="slide closing">
  <svg class="photo closing-photo" viewBox="0 0 700 607" role="img" aria-label="Glowing AI processor chip on a dark circuit board">
    <defs>
      <radialGradient id="chipGlow" cx="40%" cy="55%" r="70%">
        <stop offset="0" stop-color="#2f5fe0"/>
        <stop offset=".45" stop-color="#13245a"/>
        <stop offset="1" stop-color="#070d22"/>
      </radialGradient>
    </defs>
    <path d="M0 0 H640 C560 60 520 140 560 240 C600 340 560 430 480 480 C430 515 460 570 500 607 H0 Z" fill="url(#chipGlow)"/>
  </svg>
  <div class="closing-name">KINDREDAI</div>
  <div class="thanks">THANK YOU</div>
  <div class="presenter">PRESENTER NAME</div>
  <ul class="contacts">
    <li><svg viewBox="0 0 16 16"><path d="M3.5 1.5l2.5 0 1.2 3.2-1.6 1.2c.8 1.8 2.2 3.2 4 4l1.2-1.6 3.2 1.2v2.5c0 .8-.7 1.5-1.5 1.5C6.8 13.5 2.5 9.2 2 3c0-.8.7-1.5 1.5-1.5z"/></svg>(555) 014 207</li>
    <li><svg viewBox="0 0 16 16"><circle cx="8" cy="8" r="6.5" fill="none" stroke="#222" stroke-width="1.6"/><path d="M4 6c2 0 2 2 3.5 2S9 10 8 13M10 3c0 2 2 2 4 3" fill="none" stroke="#222" stroke-width="1.4"/></svg>www.kindredai.example</li>
    <li><svg viewBox="0 0 16 16"><rect x="1" y="3" width="14" height="10" rx="1"/><path d="M1.5 4l6.5 5 6.5-5" fill="none" stroke="#fff" stroke-width="1.2"/></svg>info@kindredai.example</li>
    <li><svg viewBox="0 0 16 16"><path d="M8 1a5 5 0 0 0-5 5c0 4 5 9 5 9s5-5 5-9a5 5 0 0 0-5-5zm0 7a2 2 0 1 1 0-4 2 2 0 0 1 0 4z"/></svg>123,Lorem ipsum dolor sit amet, consectetur<br>adipiscing elit</li>
  </ul>
</section>

</body>
</html>
```